Tulmex Business Card

I already have the conplay logo. I need to develop a professional business card layout

Target Market(s)

Business

Industry/Entity Type

Business

Contact Information for Business Card

Company Name: Tulmex Limited

Font styles to use
Sans Serif

Colors

Designer to choose colors to be used in the design.

Requirements
Must have
• Use current logo
• Need two card size options:
• Small Card: 70mm x 28mm (Landscape)
• Square Card: 65mm x 65mm
Nice to have
• I will need 8-10 files for each name, number and email address (details to follow)

```html
<!DOCTYPE html>
<html lang="en">
<head>
<meta charset="utf-8">
<title>Tulmex Business Card</title>
<link href="https://fonts.googleapis.com/css2?family=Roboto:wght@400;500;700;900&display=swap" rel="stylesheet">
<style>
  :root {
    --stage: #6f5239;
    --card-white: #ffffff;
    --navy: #1f1f8c;
    --text-grey: #555555;
    --icon-green: #1e7a3c;
    --brand-green: #2a8f3a;
    --glow-light: #8cc63f;
    --glow-dark: #006b35;
    --white: #ffffff;
  }
  html, body {
    margin: 0;
    padding: 0;
    width: 1200px;
    height: 960px;
    overflow: hidden;
    background: var(--stage);
    font-family: "Roboto", Arial, sans-serif;
  }
  .stage {
    position: relative;
    width: 1200px;
    height: 960px;
  }
  .card {
    position: absolute;
    width: 384px;
    height: 384px;
    box-shadow: 0 3px 6px rgba(0,0,0,0.35);
    overflow: hidden;
  }
  .card-front {
    left: 249px;
    top: 294px;
    background: var(--card-white);
  }
  .front-art {
    position: absolute;
    inset: 0;
  }
  .holder-name {
    position: absolute;
    right: 29px;
    top: 24px;
    margin: 0;
    color: var(--white);
    font-size: 20px;
    font-weight: 500;
    letter-spacing: 0.2px;
  }
  .brand-name {
    position: absolute;
    left: 29px;
    top: 198px;
    margin: 0;
    color: var(--brand-green);
    font-size: 44px;
    font-weight: 900;
    line-height: 1;
    letter-spacing: 1px;
  }
  .address {
    position: absolute;
    left: 30px;
    top: 259px;
    margin: 0;
    color: var(--text-grey);
    font-size: 14.5px;
    line-height: 18px;
    font-style: normal;
  }
  .contacts {
    position: absolute;
    left: 30px;
    top: 303px;
    margin: 0;
    padding: 0;
    list-style: none;
    color: var(--text-grey);
    font-size: 14.5px;
  }
  .contacts li {
    display: flex;
    align-items: center;
    height: 19.5px;
  }
  .contacts svg {
    width: 12px;
    height: 12px;
    margin-right: 9px;
    fill: var(--icon-green);
  }
  .card-back {
    left: 672px;
    top: 296px;
    background: radial-gradient(circle at 50% 50%, var(--glow-light) 0%, #4aa032 30%, var(--glow-dark) 72%);
    display: flex;
    align-items: center;
    justify-content: center;
  }
  .back-brand {
    margin: 0 0 8px;
    color: var(--white);
    font-size: 46px;
    font-weight: 900;
    letter-spacing: 1px;
  }
</style>
</head>
<body>
<main class="stage">
  <section class="card card-front">
    <svg class="front-art" viewBox="0 0 384 384" width="384" height="384">
      <path d="M0 0 H384 V166 Q230 38 0 62 Z" fill="var(--navy)"/>
      <path d="M0 62 Q230 38 384 166" fill="none" stroke="var(--white)" stroke-width="1.5"/>
    </svg>
    <h2 class="holder-name">MARCUS HALE</h2>
    <p class="brand-name">TULMEX</p>
    <address class="address">2140 Juniper Court<br>Fairbanks, Alaska 34512</address>
    <ul class="contacts">
      <li><svg viewBox="0 0 12 12"><path d="M2.5 0.5 L4.5 0.5 L5.3 3.2 L4 4.3 Q5 6.8 7.7 8 L8.8 6.7 L11.5 7.5 L11.5 9.5 Q11 11.5 9 11.5 Q0.5 10.5 0.5 2.5 Q0.5 0.8 2.5 0.5 Z"/></svg>689 555 0192</li>
      <li><svg viewBox="0 0 12 12"><path d="M0 2.5 H12 V10 H0 Z M0.8 3.2 L6 6.8 L11.2 3.2 L11.2 3.8 L6 7.6 L0.8 3.8 Z" fill-rule="evenodd"/></svg>marcus@tulmex.com</li>
      <li><svg viewBox="0 0 12 12"><circle cx="6" cy="6" r="5.5"/><path d="M3 3 Q5 4 4.5 6 Q6 7 5.5 9.5 M8 2.5 Q7 4.5 9 5.5" stroke="var(--white)" stroke-width="1" fill="none"/></svg>www.tulmex.com</li>
    </ul>
  </section>
  <section class="card card-back">
    <p class="back-brand">TULMEX</p>
  </section>
</main>
</body>
</html>
```